Stationery Design Project

We are looking for a full revision of our existing stationary to include within this project:

- Letterhead
- Business card
- Compliment slip

The items should be a reflection of our new website which can be found at http://www.larkfieldchecks.co.uk/

Our logo files are included within the file brief

There are some further projects which we may approach the winning designer for as we need a revision to the front cover of our reports, a new price list and two brochures for specific target markets.

Industry/Entity Type

Business

```html
<!DOCTYPE html>
<html lang="en">
<head>
<meta charset="utf-8">
<title>Larkfield Checks – Stationery</title>
<link rel="stylesheet" href="https://fonts.googleapis.com/css2?family=Josefin+Sans:wght@300;400;600&display=swap">
<style>
  :root {
    --backdrop: #ebebeb;
    --paper: #ffffff;
    --ink-navy: #2e2a64;
    --ink-violet: #5d4d7e;
    --band-dark: #2f2553;
    --card-left: #30244d;
    --card-right: #3b4f9c;
    --card-text: #d4d8f0;
    --shadow: 6px 7px 7px rgba(30, 25, 30, 0.5);
  }
  * { margin: 0; padding: 0; box-sizing: border-box; }
  html, body {
    width: 1200px; height: 728px; overflow: hidden;
    background: var(--backdrop);
    font-family: "Josefin Sans", "Helvetica Neue", Arial, sans-serif;
  }
  .sheet-set { position: relative; width: 1200px; height: 728px; }

  .piece { position: absolute; background: var(--paper); box-shadow: var(--shadow); overflow: hidden; }
  .piece svg.rule { position: absolute; inset: 0; width: 100%; height: 100%; }

  .wordmark {
    position: absolute;
    font-weight: 600;
    text-transform: uppercase;
    color: var(--ink-navy);
    letter-spacing: 0.02em;
    white-space: nowrap;
    line-height: 1;
  }
  .contact-list { position: absolute; list-style: none; text-transform: uppercase; font-weight: 300; }

  /* Letterhead */
  .letterhead { left: 151px; top: 44px; width: 472px; height: 607px; }
  .letterhead .wordmark { left: 16px; top: 28px; font-size: 27px; }
  .letterhead .contact-list { left: 312px; top: 12px; font-size: 10px; line-height: 10.5px; color: var(--ink-violet); font-weight: 400; }

  /* Compliment slip */
  .compliment-slip { left: 35px; top: 400px; width: 504px; height: 203px; }
  .compliment-slip .title-band {
    position: absolute; left: 0; top: 0; width: 100%; height: 19px;
    background: var(--band-dark); color: var(--paper);
    font-size: 17px; font-weight: 400; text-transform: uppercase; letter-spacing: 0.04em;
    text-align: right; padding-right: 8px; line-height: 21px;
  }
  .compliment-slip .contact-list { left: 1px; top: 46px; font-size: 15px; line-height: 17.5px; color: var(--ink-navy); }
  .compliment-slip .wordmark { left: 8px; top: 174px; font-size: 22px; }

  /* Business card front */
  .card-front { left: 656px; top: 104px; width: 471px; height: 253px; }
  .card-front .wordmark { left: 44px; top: 212px; font-size: 33px; }

  /* Business card back */
  .card-back {
    left: 657px; top: 393px; width: 471px; height: 250px;
    background: linear-gradient(90deg, var(--card-left) 0%, var(--card-left) 22%, #37306a 55%, var(--card-right) 100%);
  }
  .card-back .contact-list { left: 352px; top: 108px; font-size: 17px; line-height: 21.5px; color: var(--card-text); }
</style>
</head>
<body>
<main class="sheet-set">

  <section class="piece letterhead" aria-label="Letterhead">
    <svg class="rule" viewBox="0 0 472 607" aria-hidden="true">
      <path d="M8 84 Q 90 62 220 72 L 374 100 L 472 62" fill="none" stroke="var(--ink-navy)" stroke-width="4"/>
    </svg>
    <div class="wordmark">Larkfield Checks</div>
    <ul class="contact-list">
      <li>Phone</li><li>Fax</li><li>Web</li><li>Address</li><li>Name</li>
    </ul>
  </section>

  <section class="piece compliment-slip" aria-label="Compliment slip">
    <div class="title-band">With Compliments</div>
    <ul class="contact-list">
      <li>Phone</li><li>Fax</li><li>Web</li><li>Address</li><li>Name</li>
    </ul>
    <div class="wordmark">Larkfield Checks</div>
  </section>

  <section class="piece card-front" aria-label="Business card front">
    <div class="wordmark">Larkfield Checks</div>
  </section>

  <section class="piece card-back" aria-label="Business card back">
    <svg class="rule" viewBox="0 0 471 250" aria-hidden="true">
      <path d="M14 228 Q 110 196 240 206 L 336 226 L 471 202" fill="none" stroke="var(--paper)" stroke-width="4"/>
    </svg>
    <ul class="contact-list">
      <li>Phone</li><li>Fax</li><li>Web</li><li>Address</li><li>Name</li>
    </ul>
  </section>

</main>
</body>
</html>
```